I need a compelling, relevant cover for a book being published in January - title is the name of this project. The book is a call to action to women to become entrepreneurs as today's best path to achieving parity, purpose, prosperity and passion. See extended description of the book's message online at:
walkingtallneverrequireswalkingalone.example
(and attached pdf -- the cover art posted here is simply a placeholder/clip art ). I'm looking for something more emotional and exciting and distinctive and appropriate to the subject matter and message..
type on cover must include:
Standing Tall Won't Require Standing Alone
By Marcia T. Vellby
How Trusting Your Own Instincts Can Shift Your Path and Build Your Venture
With a Foreword by CEO Dorinda P. Halvorsen

Target Market(s)

Professional women, women business owners, aspiring women students, marketers who target women in business, such as IT providers; lenders and funders; financial services like credit card issuers -- anyone who sells to women i biz. Women's networking groups,entrepreneurship divisions at universities, and associations. International audience but tilted toward US readers.

Industry/Entity Type

Call

Font styles to use
Serif

Requirements
Nice to have
• Something that stands out from the crowd -- that would make a woman want to pick up the book because it "speaks" her language/values. Something that addresses contemporary, up-to-date ideas about gender equity/sex roles/women's advancement
Should not have
• NOTHING PINK! Please avoid "empowerment" looks and ideas (too cliche) and avoid traditional business images, like briefcases

```html
<!DOCTYPE html>
<html lang="en">
<head>
<meta charset="utf-8">
<title>Standing Tall Won't Require Standing Alone — Book Cover</title>
<link rel="stylesheet" href="https://fonts.googleapis.com/css2?family=Playfair+Display:wght@700;800&display=swap">
<style>
  :root {
    --stone: #aaa7a8;
    --stone-light: #b8b5b6;
    --stone-dark: #9a9798;
    --ember: #e27b2f;
    --chalk: #ffffff;
    --sun: #f4dc2c;
    --sun-soft: #f6e27a;
    --ember-soft: #d98a5a;
  }
  html, body {
    margin: 0;
    padding: 0;
    width: 759px;
    height: 1200px;
    overflow: hidden;
    background: var(--stone);
  }
  .cover {
    position: relative;
    width: 759px;
    height: 1200px;
    overflow: hidden;
    background: radial-gradient(ellipse at 45% 55%, var(--stone-light) 0%, var(--stone) 55%, var(--stone-dark) 100%);
    font-family: "Playfair Display", Georgia, serif;
  }
  .rule {
    position: absolute;
    height: 6px;
    background: var(--sun);
  }
  .rule--top-long { left: 0; top: 78px; width: 142px; }
  .rule--top-short { left: 0; top: 130px; width: 96px; }
  .rule--mark { background: var(--ember-soft); height: 4px; opacity: .8; }
  .rule--mark-a { left: 519px; top: 176px; width: 68px; }
  .rule--mark-b { left: 519px; top: 202px; width: 68px; }
  .rule--foreword-top { left: 455px; top: 803px; width: 228px; }
  .rule--foreword-bottom { left: 455px; top: 884px; width: 304px; }

  .title {
    position: absolute;
    left: 74px;
    top: 262px;
    margin: 0;
    font-weight: 700;
    font-size: 70px;
    line-height: 68px;
    color: var(--ember);
    letter-spacing: -0.5px;
  }
  .title .accent { color: var(--chalk); }

  .subtitle {
    position: absolute;
    left: 76px;
    top: 508px;
    width: 640px;
    margin: 0;
    font-weight: 700;
    font-size: 30px;
    line-height: 46px;
    color: var(--chalk);
  }

  .foreword {
    position: absolute;
    right: 78px;
    top: 843px;
    margin: 0;
    font-weight: 700;
    font-size: 14px;
    color: var(--ember);
  }

  .author {
    position: absolute;
    right: 76px;
    top: 1128px;
    margin: 0;
    font-weight: 700;
    font-size: 32px;
    color: var(--ember);
  }

  .steps {
    position: absolute;
    border-radius: 40%;
  }
  .steps--faint {
    left: 248px; top: 556px; width: 60px; height: 46px;
    background: radial-gradient(ellipse, rgba(226,123,47,.45) 0%, rgba(226,123,47,0) 70%);
  }
  .steps--bright {
    left: 70px; top: 945px; width: 150px; height: 175px;
    background: radial-gradient(ellipse, rgba(246,226,122,.9) 0%, rgba(244,220,44,.35) 50%, rgba(244,220,44,0) 75%);
  }
</style>
</head>
<body>
  <main class="cover">
    <div class="rule rule--top-long"></div>
    <div class="rule rule--top-short"></div>
    <div class="rule rule--mark rule--mark-a"></div>
    <div class="rule rule--mark rule--mark-b"></div>

    <h1 class="title">Standing <span class="accent">Tall</span><br>Won't Require<br>Standing Alone</h1>

    <p class="subtitle">How trusting your own instincts can shift your path and build your venture.</p>

    <div class="steps steps--faint" role="img" aria-label="Faint orange footprints walking up the cover"></div>

    <div class="rule rule--foreword-top"></div>
    <p class="foreword">Foreword by CEO Dorinda P. Halvorsen</p>
    <div class="rule rule--foreword-bottom"></div>

    <div class="steps steps--bright" role="img" aria-label="Pair of glowing yellow footprints"></div>

    <p class="author">By Marcia T. Vellby</p>
  </main>
</body>
</html>
```